Modern Design Business Card industrial maintenance company

Business card design for Company named Brookvale Equipment Services

Target Market(s)

Industrial

Industry/Entity Type

Maintenance and repair

Contact Information for Business Card

Place holder for address, office phone, mobile number and email

Requirements
Must have
• Clean modern look
Nice to have
• N/a

```html
<!DOCTYPE html>
<html lang="en">
<head>
<meta charset="UTF-8">
<title>Brookvale Equipment Services – Business Card</title>
<link href="https://fonts.googleapis.com/css2?family=Montserrat:wght@400;500;700&display=swap" rel="stylesheet">
<style>
  :root {
    --page-bg: #e9e6e1;
    --card-bg: #1e1e1e;
    --card-shadow: rgba(0, 0, 0, 0.35);
    --ink-light: #ffffff;
    --ink-soft: #e4e4e4;
    --pattern-dark: #141414;
    --pattern-mid: #262626;
    --pattern-light: #6a6a6a;
  }
  * { box-sizing: border-box; margin: 0; padding: 0; }
  html, body {
    width: 900px; height: 1200px; overflow: hidden;
    background: var(--page-bg);
    font-family: "Montserrat", Arial, sans-serif;
  }
  .card {
    position: absolute; left: 80px; width: 742px; height: 442px;
    border-radius: 18px; overflow: hidden;
    background: var(--card-bg);
    box-shadow: 0 10px 24px var(--card-shadow);
  }
  .card--front { top: 130px; }
  .card--back { top: 638px; }

  .company { position: absolute; left: 36px; top: 74px; color: var(--ink-light); font-weight: 500; }
  .company__main { display: block; font-size: 27px; letter-spacing: 2px; line-height: 1; }
  .company__sub { display: block; font-size: 11.5px; letter-spacing: 4.2px; margin-top: 6px; }

  .person { position: absolute; left: 37px; top: 158px; color: var(--ink-light); }
  .person__name { font-size: 22px; font-weight: 700; letter-spacing: 0.5px; }
  .person__role { font-size: 14px; font-weight: 400; margin-top: 8px; color: var(--ink-soft); letter-spacing: 0.5px; }

  .address { position: absolute; left: 37px; top: 240px; color: var(--ink-soft); font-size: 15px; line-height: 20px; }

  .contacts { position: absolute; left: 37px; top: 306px; list-style: none; color: var(--ink-soft); font-size: 15px; }
  .contacts__item { display: flex; align-items: center; height: 28px; }
  .contacts__item:nth-child(3) { height: 26px; }
  .contacts__icon { width: 15px; height: 15px; margin-right: 12px; fill: var(--ink-light); }

  .brand-ring { position: absolute; right: 0; top: 0; width: 260px; height: 442px; }

  .back-pattern {
    position: absolute; inset: 0;
    background: linear-gradient(200deg, var(--pattern-light) 0%, var(--pattern-mid) 38%, var(--pattern-dark) 70%);
  }
</style>
</head>
<body>
  <section class="card card--front">
    <div class="company">
      <span class="company__main">BROOKVALE</span>
      <span class="company__sub">EQUIPMENT SERVICES</span>
    </div>

    <div class="person">
      <h1 class="person__name">ROWAN TESSLER</h1>
      <p class="person__role">OWNER</p>
    </div>

    <p class="address">845 Harbor Mill Road, Ste<br>210 Ashford, OH 44012</p>

    <ul class="contacts">
      <li class="contacts__item">
        <svg class="contacts__icon" viewBox="0 0 24 24"><path d="M6.6 10.8a15.1 15.1 0 0 0 6.6 6.6l2.2-2.2c.3-.3.7-.4 1-.2 1.1.4 2.3.6 3.6.6.6 0 1 .4 1 1V20c0 .6-.4 1-1 1A17 17 0 0 1 3 4c0-.6.4-1 1-1h3.5c.6 0 1 .4 1 1 0 1.3.2 2.5.6 3.6.1.3 0 .7-.2 1z"/></svg>
        (555) 214-3087
      </li>
      <li class="contacts__item">
        <svg class="contacts__icon" viewBox="0 0 24 24"><path d="M7 1h10a2 2 0 0 1 2 2v18a2 2 0 0 1-2 2H7a2 2 0 0 1-2-2V3a2 2 0 0 1 2-2zm0 3v14h10V4zm5 15.2a1.2 1.2 0 1 0 0 2.4 1.2 1.2 0 0 0 0-2.4z"/></svg>
        (555) 630-9174
      </li>
      <li class="contacts__item">
        <svg class="contacts__icon" viewBox="0 0 24 24"><path d="M2 5h20v1.5l-10 6.5L2 6.5zm0 3.8 10 6.5 10-6.5V19H2z"/></svg>
        info@brookvale.example
      </li>
      <li class="contacts__item">
        <svg class="contacts__icon" viewBox="0 0 24 24"><path d="M12 2a10 10 0 1 0 0 20 10 10 0 0 0 0-20zm-1 17.9A8 8 0 0 1 4.1 10L9 15v1a2 2 0 0 0 2 2zm6.9-2.5A2 2 0 0 0 16 16h-1v-3a1 1 0 0 0-1-1H8v-2h2a1 1 0 0 0 1-1V7h2a2 2 0 0 0 2-2v-.4a8 8 0 0 1 2.9 12.8z"/></svg>
        www.brookvale.example
      </li>
    </ul>

    <svg class="brand-ring" viewBox="0 0 260 442" aria-hidden="true">
      <circle cx="262" cy="222" r="248" fill="none" stroke="var(--ink-light)" stroke-width="16"/>
    </svg>
  </section>

  <section class="card card--back">
    <div class="back-pattern" role="img" aria-label="Repeating spot-gloss pattern of the company emblem on black, fading to a silver sheen toward the upper right"></div>
  </section>
</body>
</html>
```